Business Card and Letterhead Design for Public Accounting Firm

Business card and letterhead design for a CPA Firm located in Orange County, CA. We're looking for a modern and professional design utilizing our existing logo. We'd like a clean "less is more" look, but also something that catches the eye. We provide a high level of service to our clients. Open to single or double sided business cards.

Additional info: color numbers on logo
Blue :
R 0
G 83
B 125

#00537D

Silver :

R 154
G 154
B 154

#9A9A9A

Target Market(s)

Businesses and individuals

Industry/Entity Type

Accounting

Contact Information for Business Card

Moss Whitfield & Danby LLP - 4827 Larkspur Vale Road, Irvine, CA 92614 - (949)731-2864 - mwdaccts.example

Font styles to use
Serif
Sans Serif
Other font styles liked:
• See font file uploaded

Colors
0054AA
0677BA
7BADD7
CADEEF
E8F1F8

Requirements
Nice to have
• Possibly use the font file provided which matches our logo, but adjust to be not in all caps

```html
<!DOCTYPE html>
<html lang="en">
<head>
<meta charset="utf-8">
<title>Moss Whitfield &amp; Danby LLP – Letterhead</title>
<link href="https://fonts.googleapis.com/css2?family=Lato:wght@400;700&family=Cormorant+Garamond:wght@500&family=Satisfy&display=swap" rel="stylesheet">
<style>
  :root {
    --backdrop: #e4e4e4;
    --paper: #ffffff;
    --brand-blue: #00537d;
    --brand-silver: #9a9a9a;
    --ink: #2b2b2b;
    --ink-soft: #555555;
  }
  * { box-sizing: border-box; margin: 0; padding: 0; }
  html, body {
    width: 1200px; height: 874px; overflow: hidden;
    background: var(--backdrop);
  }
  .letterhead {
    position: absolute;
    left: 320px; top: 72px;
    width: 560px; height: 730px;
    background: var(--paper);
    box-shadow: 0 2px 10px rgba(0,0,0,0.08);
    font-family: "Lato", sans-serif;
    color: var(--ink);
  }
  .firm-contact {
    position: absolute;
    right: 54px; top: 40px;
    font-family: "Cormorant Garamond", serif;
    font-variant: small-caps;
    font-size: 10px;
    line-height: 1.35;
    color: var(--ink-soft);
    letter-spacing: 0.3px;
  }
  .contact-line { display: flex; align-items: center; gap: 5px; }
  .contact-icon { width: 9px; height: 9px; }
  .firm-mark {
    position: absolute;
    left: 48px; top: 110px;
    display: flex; align-items: center; gap: 8px;
  }
  .firm-mark-square {
    width: 14px; height: 14px;
    background: var(--brand-blue);
  }
  .firm-mark-name {
    font-family: "Lato", sans-serif;
    font-weight: 400;
    font-size: 17px;
    letter-spacing: 1.5px;
    color: var(--brand-blue);
  }
  .letter {
    position: absolute;
    left: 70px; top: 190px;
    width: 430px;
    font-size: 9.6px;
    line-height: 1.3;
  }
  .letter-date { margin-bottom: 14px; font-size: 10.5px; }
  .recipient { margin-bottom: 12px; font-size: 10.5px; }
  .salutation { font-weight: 700; font-size: 12.5px; margin: 4px 0 14px; }
  .letter p.body-copy { margin-bottom: 14px; }
  .closing { margin-top: 12px; color: var(--ink-soft); }
  .signature {
    font-family: "Satisfy", cursive;
    font-size: 30px;
    margin-top: 6px;
    margin-left: 20px;
    color: var(--ink);
  }
</style>
</head>
<body>
  <main class="letterhead">
    <address class="firm-contact">
      <div>Moss Whitfield &amp; Danby LLP</div>
      <div>4827 Larkspur Vale Road</div>
      <div>Irvine, CA 92614</div>
      <div class="contact-line">
        <svg class="contact-icon" viewBox="0 0 10 10" aria-hidden="true">
          <circle cx="5" cy="5" r="5" fill="var(--brand-blue)"/>
          <path d="M3.2 2.6 L4.2 2.6 L4.6 3.8 L4 4.3 Q4.6 5.5 5.7 6 L6.2 5.4 L7.4 5.8 L7.4 6.8 Q5.5 7.2 3.9 5.6 Q2.8 4.3 3.2 2.6 Z" fill="#fff"/>
        </svg>
        <span>(949) 731-2864</span>
      </div>
      <div class="contact-line">
        <svg class="contact-icon" viewBox="0 0 10 10" aria-hidden="true">
          <circle cx="5" cy="5" r="5" fill="var(--brand-blue)"/>
          <circle cx="5" cy="5" r="3" fill="none" stroke="#fff" stroke-width="0.7"/>
          <path d="M2 5 H8 M5 2 Q3.5 5 5 8 M5 2 Q6.5 5 5 8" fill="none" stroke="#fff" stroke-width="0.6"/>
        </svg>
        <span>www.mwdaccts.example</span>
      </div>
    </address>

    <div class="firm-mark">
      <span class="firm-mark-square"></span>
      <span class="firm-mark-name">MOSS WHITFIELD &amp; DANBY LLP</span>
    </div>

    <article class="letter">
      <div class="letter-date">Feb-03-2022</div>
      <div class="recipient">Mr. Owen Lark<br>President</div>
      <div class="recipient">Fernhill Corporation<br>123 Street Name, Suite# 10<br>City, State, 120023</div>
      <div class="salutation">Dear Mr. Lark</div>
      <p class="body-copy">Lorem ipsum dolor sit amet, consectetur adipisicing elit, sed do eiusmod tempor incididunt ut labore et dolore magna aliqua. Ut enim ad minim veniam, quis nostrud exercitation ullamco laboris nisi ut aliquip ex ea commodo consequat. Duis aute irure dolor in reprehenderit in voluptate velit esse cillum dolore eu fugiat nulla pariatur.</p>
      <p class="body-copy">Lorem ipsum dolor sit amet, consectetur adipisicing elit, sed do eiusmod tempor incididunt ut labore et dolore magna aliqua. Ut enim ad minim veniam, quis nostrud exercitation ullamco laboris nisi ut aliquip ex ea commodo consequat. Duis aute irure dolor in reprehenderit in voluptate velit esse cillum dolore eu fugiat nulla pariatur.</p>
      <p class="body-copy">Lorem ipsum dolor sit amet, consectetur adipisicing elit, sed do eiusmod tempor incididunt ut labore et dolore magna aliqua. Ut enim ad minim veniam, quis nostrud exercitation ullamco laboris nisi ut aliquip ex ea commodo consequat.</p>
      <p class="body-copy">Excepteur sint occaecat cupidatat non proident, sunt in culpa qui officia deserunt mollit anim id est laborum. re et dolore magnam aliquam quaerat voluptatem.</p>
      <div class="closing">Regards</div>
      <div class="signature">Daniel Hart</div>
    </article>
  </main>
</body>
</html>
```